Firm Stationery Design

I need a design for stationery, including: Stationery First Page, Stationery Second Sheet, Envelope, Mailing Label for Flat Envelopes, and Business Cards

```html
<!DOCTYPE html>
<html lang="en">
<head>
<meta charset="utf-8">
<title>Marlow Law LLC — Stationery</title>
<link href="https://fonts.googleapis.com/css2?family=Montserrat:wght@500;600;700&family=Roboto:wght@400;500&display=swap" rel="stylesheet">
<style>
  :root{
    --orange:#ffa000;
    --ink:#1c1c1c;
    --paper:#ffffff;
    --bg:#efefef;
    --bg-low:#ececec;
    --muted:#a9a9a9;
    --text:#555555;
    --window:#cfcfcf;
  }
  *{margin:0;padding:0;box-sizing:border-box}
  html,body{width:1200px;height:800px;overflow:hidden}
  body{font-family:"Roboto",Arial,sans-serif;color:var(--ink);background:var(--bg)}
  .board{position:relative;width:1200px;height:800px;overflow:hidden}
  .backdrop{position:absolute;inset:0}
  .item{position:absolute;background:var(--paper);box-shadow:0 14px 22px rgba(0,0,0,.16)}
  .item.dark{background:var(--ink)}

  /* brand lockup */
  .brand{display:flex;flex-direction:column;align-items:center;font-family:"Montserrat",sans-serif}
  .brand-mark{background:var(--orange)}
  .brand-name{font-weight:700;color:var(--ink);text-transform:uppercase;text-align:center;line-height:1.1;letter-spacing:.02em}
  .dark .brand-name{color:var(--paper)}

  .hero-brand{position:absolute;left:98px;top:140px;width:200px}
  .hero-brand .brand-mark{width:46px;height:46px;margin-bottom:14px}
  .hero-brand .brand-name{font-size:27px}
  .intro{position:absolute;left:58px;top:316px;width:280px;text-align:center;font-size:6.2px;line-height:8.6px;color:var(--muted)}

  /* business cards */
  .card{left:63px;width:268px;height:152px}
  .card-front{top:428px}
  .card-back{top:615px}
  .card .brand{position:absolute;left:18px;top:19px;width:70px}
  .card .brand-mark{width:18px;height:18px;margin-bottom:5px}
  .card .brand-name{font-size:9px}
  .card-back .brand{left:99px;top:52px}
  .holder{position:absolute;left:160px;top:30px}
  .holder-name{font-family:"Montserrat",sans-serif;font-weight:600;font-size:12.5px}
  .holder-role{font-size:5.8px;color:var(--orange);margin-top:1px}
  .card-rule{position:absolute;left:18px;right:18px;top:88px;height:1px;background:var(--orange)}
  .contact{display:flex;align-items:center;gap:5px;font-size:6px;color:#333}
  .contact svg{width:7px;height:7px;flex:none}
  .card-contacts{position:absolute;left:18px;top:100px;display:flex;flex-direction:column;gap:6px}
  .card-address{position:absolute;left:155px;top:100px;align-items:flex-start;line-height:8px}
  .bar{position:absolute;left:0;bottom:0;width:100%;display:block}

  /* letterhead */
  .letterhead{left:454px;top:68px;width:329px;height:442px}
  .letterhead .top-bar{position:absolute;left:0;top:0;width:100%}
  .letterhead .brand{position:absolute;left:34px;top:38px;width:62px}
  .letterhead .brand-mark{width:20px;height:20px;margin-bottom:5px}
  .letterhead .brand-name{font-size:8.5px}
  .date{position:absolute;right:40px;top:47px;font-size:4.6px;font-weight:500;color:var(--orange)}
  .recipient{position:absolute;left:40px;top:98px;font-size:4.3px;line-height:6.6px;color:var(--text)}
  .recipient .name{color:var(--orange);font-weight:500}
  .recipient .org{color:var(--ink);font-size:4.8px;margin-top:4px}
  .body-copy{position:absolute;left:40px;top:163px;width:250px;font-size:5px;line-height:6.8px;letter-spacing:.06em;color:var(--text)}
  .body-copy p{margin-bottom:9.5px}
  .signature{position:absolute;left:42px;top:322px;width:48px;height:20px;background:linear-gradient(90deg,#ececec,#f6f6f6);border-radius:3px}
  .signer{position:absolute;left:42px;top:347px;font-size:5.2px;line-height:6px;color:var(--text)}
  .signer b{font-weight:500;color:#333}
  .sheet-contacts{position:absolute;left:207px;top:338px;display:flex;flex-direction:column;gap:10px}
  .sheet-contacts .contact,.env-contacts .contact{font-size:4.2px;line-height:6px;color:var(--text);gap:9px}

  /* second sheet */
  .second-sheet{left:817px;top:68px;width:329px;height:442px}
  .second-sheet .brand{position:absolute;left:27px;top:30px;width:62px}
  .second-sheet .brand-mark{width:20px;height:20px;margin-bottom:6px}
  .second-sheet .brand-name{font-size:9px}

  /* envelopes */
  .envelope{left:454px;top:546px;width:331px;height:172px}
  .envelope .brand{position:absolute;left:17px;top:18px;width:62px}
  .envelope .brand-mark{width:20px;height:20px;margin-bottom:5px}
  .envelope .brand-name{font-size:8.5px}
  .env-contacts{position:absolute;left:17px;top:96px;display:flex;flex-direction:column;gap:7px}
  .address-window{position:absolute;left:180px;top:91px;width:117px;height:53px;background:var(--window);border-radius:3px}
  .envelope-back{left:815px;top:546px;width:331px;height:172px}
  .flap{position:absolute;left:0;top:0;width:100%}
  .envelope-back .brand-mark{position:absolute;left:158px;top:20px;width:16px;height:16px}
</style>
</head>
<body>
<main class="board">
  <svg class="backdrop" width="1200" height="800" aria-hidden="true">
    <rect width="1200" height="800" fill="var(--bg)"/>
    <rect x="0" y="400" width="400" height="400" fill="var(--bg-low)"/>
    <polygon points="1132,0 1200,0 1200,800 400,800 400,400 800,400" fill="var(--orange)"/>
  </svg>

  <section class="brand hero-brand">
    <span class="brand-mark"></span>
    <span class="brand-name">Marlow Law LLC</span>
  </section>
  <p class="intro">We're here to provide the residents of Lakeview County and Riverbend Parish with an alternative to banking. You will find your financial needs in a modest, reasonable and balanced means. We offer friendly, small-town financial service with a dash of technology in the mix, so you can easily keep up with your finances</p>

  <!-- business card front -->
  <article class="item card card-front">
    <div class="brand"><span class="brand-mark"></span><span class="brand-name">Marlow Law LLC</span></div>
    <div class="holder"><div class="holder-name">yourname</div><div class="holder-role">Director</div></div>
    <div class="card-rule"></div>
    <div class="card-contacts">
      <div class="contact"><svg viewBox="0 0 10 10"><path d="M2 1l2 2-1 1.3c.6 1.3 1.4 2.1 2.7 2.7L7 6l2 2-1.3 1.3C4.5 9 1 5.5.7 2.3z" fill="var(--orange)"/></svg>123 456 7890</div>
      <div class="contact"><svg viewBox="0 0 10 10"><circle cx="5" cy="5" r="4.2" fill="none" stroke="var(--orange)"/><path d="M1 5h8M5 .8c-2.2 2.5-2.2 5.9 0 8.4M5 .8c2.2 2.5 2.2 5.9 0 8.4" fill="none" stroke="var(--orange)" stroke-width=".7"/></svg>www.yourname.com</div>
      <div class="contact"><svg viewBox="0 0 10 10"><rect x=".5" y="2" width="9" height="6.5" rx="1" fill="var(--orange)"/></svg>yourname@mailbox.com</div>
    </div>
    <div class="contact card-address"><svg viewBox="0 0 10 10"><path d="M5 .5a3.3 3.3 0 0 1 3.3 3.3C8.3 6.3 5 9.5 5 9.5S1.7 6.3 1.7 3.8A3.3 3.3 0 0 1 5 .5z" fill="var(--orange)"/><circle cx="5" cy="3.8" r="1.2" fill="#fff"/></svg><span>2150 Harbor Avenue, Suite 4<br>Denton, TX 76201</span></div>
    <svg class="bar" width="268" height="10" viewBox="0 0 268 10" preserveAspectRatio="none"><polygon points="0,0 160,0 156,3 0,3" fill="var(--ink)"/><polygon points="0,4 158,4 162,0 268,0 268,10 0,10" fill="var(--orange)"/></svg>
  </article>

  <!-- business card back -->
  <article class="item dark card card-back">
    <div class="brand"><span class="brand-mark"></span><span class="brand-name">Marlow Law LLC</span></div>
    <svg class="bar" width="268" height="10" viewBox="0 0 268 10" preserveAspectRatio="none"><polygon points="0,1 160,1 157,4 0,4" fill="var(--orange)"/><polygon points="162,1 268,1 268,4 159,4" fill="var(--paper)"/></svg>
  </article>

  <!-- letterhead first page -->
  <article class="item letterhead">
    <svg class="top-bar" width="329" height="14" viewBox="0 0 329 14"><polygon points="0,0 329,0 329,5 136,5 131,13 0,13" fill="var(--orange)"/><polygon points="138,9 329,9 329,13 135,13" fill="var(--ink)"/></svg>
    <div class="brand"><span class="brand-mark"></span><span class="brand-name">Marlow Law LLC</span></div>
    <div class="date">Friday, 01/01/2024</div>
    <div class="recipient">
      <div>To:</div>
      <div class="name">Daniel Reyes</div>
      <div>Creativ Director</div>
      <div class="org">Northfieldstudio.com</div>
      <div>123 Street Name TownCity</div>
      <div>State,Country 556</div>
    </div>
    <div class="body-copy">
      <p>Lorem ipsum dolor sit amet, consectetur ni ut aliquip ex ea comodo conse adipiscing elit, sed do eiusmod tempor incididunt ni ut aliqip ex ea comse ut labore et dolore magna aliqua. ut enim ad minim nisi ut alip ex cosequat veniam, quis nostrud exercitation ullamco laboris veniam, qui uco laboris adipiscing elit, sed do eiusmod tempor incididunt ni ut aliqip ex ea comse nisi ut aliquip ex ea commodo consequat</p>
      <p>Lorem ipsum dolor sit amet, consectetur ni ut aliquip ex ea comodo conse adipiscing elit, sed do eiusmod tempor incididunt ni ut aliqip ex ea comse ut labore et dolore magna aliqua. ut enim ad minim nisi ut alip ex cosequat</p>
      <p>Lorem ipsum dolor sit amet, consectetur ni ut aliquip ex ea comodo conse adipiscing elit, sed do eiusmod tempor incididunt ni ut aliqip ex ea comse ut labore et dolore magna aliqua. ut enim ad minim nisi ut alip ex cosequat veniam, quis nostrud exercitation ullamco laboris</p>
      <p>adipiscing elit, sed do eiusmod tempor incididunt ni ut aliqip ex ea comse nisi ut aliquip ex ea commodo consequat</p>
    </div>
    <div class="signature" role="img" aria-label="Handwritten signature"></div>
    <div class="signer"><b>yourname</b><br>manager</div>
    <div class="sheet-contacts">
      <div class="contact"><svg viewBox="0 0 10 10"><path d="M2 1l2 2-1 1.3c.6 1.3 1.4 2.1 2.7 2.7L7 6l2 2-1.3 1.3C4.5 9 1 5.5.7 2.3z" fill="var(--orange)"/></svg><span>+999 123 456 789<br>+00 22 123 456 55</span></div>
      <div class="contact"><svg viewBox="0 0 10 10"><circle cx="5" cy="5" r="4.2" fill="none" stroke="var(--orange)"/><path d="M1 5h8M5 .8c-2.2 2.5-2.2 5.9 0 8.4M5 .8c2.2 2.5 2.2 5.9 0 8.4" fill="none" stroke="var(--orange)" stroke-width=".7"/></svg><span>188 Street Name,Town<br>State,Country 556</span></div>
      <div class="contact"><svg viewBox="0 0 10 10"><path d="M5 .5a3.3 3.3 0 0 1 3.3 3.3C8.3 6.3 5 9.5 5 9.5S1.7 6.3 1.7 3.8A3.3 3.3 0 0 1 5 .5z" fill="var(--orange)"/><circle cx="5" cy="3.8" r="1.2" fill="#fff"/></svg><span>info@yourname.com<br>www.yourname.com</span></div>
    </div>
    <svg class="bar" width="329" height="12" viewBox="0 0 329 12" preserveAspectRatio="none"><polygon points="0,1 200,1 197,4 0,4" fill="var(--orange)"/><polygon points="202,1 329,1 329,5 199,5" fill="var(--ink)"/></svg>
  </article>

  <!-- second sheet -->
  <article class="item dark second-sheet">
    <div class="brand"><span class="brand-mark"></span><span class="brand-name">Marlow Law LLC</span></div>
    <svg class="bar" width="329" height="14" viewBox="0 0 329 14" preserveAspectRatio="none"><polygon points="0,0 128,0 134,6 329,6 329,14 0,14" fill="var(--orange)"/><polygon points="131,0 329,0 329,3 134,3" fill="var(--paper)"/></svg>
  </article>

  <!-- envelope front -->
  <article class="item envelope">
    <div class="brand"><span class="brand-mark"></span><span class="brand-name">Marlow Law LLC</span></div>
    <div class="env-contacts">
      <div class="contact"><svg viewBox="0 0 10 10"><path d="M5 .5a3.3 3.3 0 0 1 3.3 3.3C8.3 6.3 5 9.5 5 9.5S1.7 6.3 1.7 3.8A3.3 3.3 0 0 1 5 .5z" fill="var(--orange)"/><circle cx="5" cy="3.8" r="1.2" fill="#fff"/></svg><span>188 Street Name,Town<br>State,Country 556</span></div>
      <div class="contact"><svg viewBox="0 0 10 10"><path d="M2 1l2 2-1 1.3c.6 1.3 1.4 2.1 2.7 2.7L7 6l2 2-1.3 1.3C4.5 9 1 5.5.7 2.3z" fill="var(--orange)"/></svg><span>+999 123 456 789<br>+00 22 123 456 55</span></div>
      <div class="contact"><svg viewBox="0 0 10 10"><circle cx="5" cy="5" r="4.2" fill="none" stroke="var(--orange)"/><path d="M1 5h8M5 .8c-2.2 2.5-2.2 5.9 0 8.4M5 .8c2.2 2.5 2.2 5.9 0 8.4" fill="none" stroke="var(--orange)" stroke-width=".7"/></svg><span>info@yourname.com<br>www.yourname.com</span></div>
    </div>
    <div class="address-window"></div>
    <svg class="bar" width="331" height="14" viewBox="0 0 331 14" preserveAspectRatio="none"><polygon points="0,0 126,0 132,5 331,5 331,14 0,14" fill="var(--orange)"/><polygon points="129,0 331,0 331,3 132,3" fill="var(--ink)"/></svg>
  </article>

  <!-- envelope back -->
  <article class="item envelope-back">
    <svg class="flap" width="331" height="56" viewBox="0 0 331 56"><path d="M0 0H331L310 44Q304 56 290 56H41Q27 56 21 44Z" fill="var(--ink)"/></svg>
    <span class="brand-mark"></span>
  </article>
</main>
</body>
</html>
```